Jolly Paws Business Card Update

I have a business card which I love. I want to keep the same logo, colours, font and style. I want to upgrade the scripting and remove some elements and add others.
On the front side under Services - remove the existing wording and insert - Providing individual coaching strategies to create happy, healthy and social canine companions
Under Rebecca Thornbury amend the current wording to read: Qualified in Dog Behavioural Training, Natural Animal Healthcare and Animal Health Science
On the reverse side to remove the web address.

```html
<!DOCTYPE html>
<html lang="en">
<head>
<meta charset="utf-8">
<title>Jolly Paws Business Card</title>
<link rel="stylesheet" href="https://fonts.googleapis.com/css2?family=Arimo:wght@400;700&display=swap">
<style>
  :root {
    --sky: #04a3e0;
    --sky-mid: #0a7fcc;
    --navy: #1f3f9f;
    --red-dark: #6e0e12;
    --red-bright: #e62226;
    --cream: #efe6c4;
    --ink: #1b1b1b;
    --white: #ffffff;
    --stage: #2b2b2d;
  }
  * { box-sizing: border-box; margin: 0; padding: 0; }
  html, body {
    width: 1200px; height: 1200px; overflow: hidden;
    background: var(--stage);
    font-family: "Arimo", Arial, sans-serif;
  }
  .sheet {
    width: 1200px; height: 1200px;
    display: flex; flex-direction: column; align-items: center; justify-content: center;
    gap: 40px;
  }
  .card {
    position: relative;
    width: 945px; height: 540px;
    overflow: hidden;
    box-shadow: 0 10px 30px rgba(0,0,0,.5);
  }
  .card svg.art { position: absolute; inset: 0; width: 100%; height: 100%; }

  /* Brand side */
  .brand-side { background: linear-gradient(180deg, var(--sky) 0%, var(--sky-mid) 45%, var(--navy) 100%); }
  .brand-lockup {
    position: absolute; left: 0; right: 0; top: 70px;
    display: flex; flex-direction: column; align-items: center;
  }
  .brand-mark {
    width: 150px; height: 150px; border-radius: 50%;
    background: var(--red-bright);
  }
  .brand-name {
    margin-top: 22px;
    font-size: 64px; font-weight: 700; letter-spacing: 3px;
    color: var(--cream); text-transform: uppercase;
  }
  .brand-tagline {
    margin-top: 8px;
    font-size: 28px; letter-spacing: 2px; color: var(--white);
  }

  /* Info side */
  .info-side { background: linear-gradient(180deg, var(--sky) 0%, var(--sky-mid) 100%); }
  .info-band {
    position: absolute; left: 0; right: 0; top: 285px; bottom: 0;
    background: linear-gradient(90deg, var(--red-dark) 0%, var(--red-bright) 45%, var(--red-dark) 100%);
  }
  .info-strip {
    position: absolute; left: 0; right: 0; top: 253px; height: 32px;
    background: var(--cream);
    color: var(--ink); font-size: 19px;
    display: flex; align-items: center; justify-content: center;
  }
  .info-brand {
    position: absolute; left: 110px; top: 95px;
    display: flex; align-items: center; gap: 18px;
  }
  .info-brand .brand-mark { width: 90px; height: 90px; }
  .info-brand .brand-name { margin: 0; font-size: 36px; letter-spacing: 1px; }
  .divider { position: absolute; width: 2px; background: var(--cream); }
  .divider.top { left: 480px; top: 70px; height: 160px; }
  .divider.bottom { left: 580px; top: 345px; height: 90px; }
  .services { position: absolute; left: 510px; top: 80px; width: 410px; color: var(--white); }
  .services h2 { font-size: 26px; font-weight: 400; letter-spacing: 1px; margin-bottom: 8px; }
  .services p { font-size: 19px; font-weight: 700; line-height: 1.3; }
  .person { position: absolute; right: 385px; top: 310px; text-align: right; width: 540px; }
  .person-name { font-size: 34px; font-weight: 700; color: var(--white); }
  .person-quals { margin-top: 10px; font-size: 18px; line-height: 1.35; color: var(--cream); }
  .contacts { position: absolute; left: 605px; top: 350px; list-style: none; color: var(--white); font-size: 23px; }
  .contacts li { display: flex; align-items: center; gap: 12px; margin-bottom: 14px; }
  .contacts svg { width: 28px; height: 28px; flex: none; }
</style>
</head>
<body>
<main class="sheet">

  <section class="card brand-side" aria-label="Business card, brand side">
    <svg class="art" viewBox="0 0 945 540" aria-hidden="true">
      <defs>
        <linearGradient id="redBand" x1="0" x2="1" y1="0" y2="0">
          <stop offset="0" stop-color="#6e0e12"/>
          <stop offset=".45" stop-color="#e62226"/>
          <stop offset="1" stop-color="#6e0e12"/>
        </linearGradient>
      </defs>
      <path d="M0 335 C 300 360 650 440 945 528 L945 540 L0 540 Z" fill="url(#redBand)"/>
      <path d="M0 328 C 300 353 650 433 945 521" fill="none" stroke="#efe6c4" stroke-width="4"/>
    </svg>
    <div class="brand-lockup">
      <div class="brand-mark"></div>
      <div class="brand-name">Jolly Paws</div>
      <div class="brand-tagline">HAPPY DOGS, HAPPY OWNERS</div>
    </div>
  </section>

  <section class="card info-side" aria-label="Business card, contact side">
    <div class="info-brand">
      <div class="brand-mark"></div>
      <div class="brand-name">Jolly Paws</div>
    </div>
    <div class="divider top"></div>
    <div class="services">
      <h2>SERVICES</h2>
      <p>Providing individual coaching strategies to create happy, healthy and social canine companions</p>
    </div>
    <div class="info-band"></div>
    <div class="info-strip">Promoting communication and connection between dogs and their families</div>
    <div class="person">
      <div class="person-name">Rebecca Thornbury</div>
      <div class="person-quals">Qualified in Dog Behavioural Training, Natural<br>Animal Healthcare and Animal Health Science</div>
    </div>
    <div class="divider bottom"></div>
    <ul class="contacts">
      <li>
        <svg viewBox="0 0 28 28" aria-hidden="true"><circle cx="14" cy="14" r="13" fill="#efe6c4"/><rect x="10" y="6" width="8" height="16" rx="2" fill="none" stroke="#9b1418" stroke-width="2"/><circle cx="14" cy="19" r="1" fill="#9b1418"/></svg>
        0417 286 530
      </li>
      <li>
        <svg viewBox="0 0 28 28" aria-hidden="true"><circle cx="14" cy="14" r="13" fill="#efe6c4"/><rect x="7" y="9" width="14" height="10" fill="none" stroke="#9b1418" stroke-width="2"/><path d="M7 9 L14 15 L21 9" fill="none" stroke="#9b1418" stroke-width="2"/></svg>
        jollypaws1@mailbox.com
      </li>
    </ul>
  </section>

</main>
</body>
</html>
```